Need a creative cover photo for social media profiles

We are rebranding and would like to promote the new look on our cover image for our social platforms (Pelmora, Quillane, Brindle). It should feel similar in brand as the attached collateral. We want this to make a statement as our new logo and feel are completely different from where we currently are. I am sending along examples of other collateral we have created.
Target Market(s)
IT, accounting professionals and companies looking to hire those professionals.
Industry/Entity Type
Staffing
Requirements
Must have
- Logo
Our corporate font is Nexa Bold for headlines and Ebrima for content.
CMYK combinations for our corporate colors
C 2. M 66, Y 87, K 0
C 84, M 69, Y 47, K 39

```html
<!DOCTYPE html>
<html lang="en">
<head>
<meta charset="utf-8">
<title>Corvane Group – Cover Options</title>
<link rel="stylesheet" href="https://fonts.googleapis.com/css2?family=Montserrat:wght@700&family=Noto+Sans:wght@400&display=swap">
<style>
  :root {
    --canvas: #000000;
    --brand-orange: #ec7a38;
    --brand-navy: #27354d;
    --brand-blue: #145aa8;
    --photo-cream: #fbf1ea;
    --photo-peach: #efd9cf;
    --photo-rose: #dcc0b6;
    --photo-shadow: rgba(120, 86, 70, 0.55);
    --text-light: #ffffff;
  }
  * { margin: 0; padding: 0; box-sizing: border-box; }
  html, body {
    width: 1034px;
    height: 1200px;
    overflow: hidden;
    background: var(--canvas);
  }
  .canvas {
    position: relative;
    width: 1034px;
    height: 1200px;
  }
  .cover {
    position: absolute;
    left: 37px;
    width: 959px;
    height: 354px;
    overflow: hidden;
  }
  .cover--orange { top: 41px; }
  .cover--navy { top: 420px; }
  .cover--blue { top: 800px; }

  .cover__photo {
    position: absolute;
    inset: 0;
    --scene:
      radial-gradient(ellipse 170px 200px at 92% 18%, var(--photo-shadow) 0%, rgba(120,86,70,0) 100%),
      radial-gradient(ellipse 260px 150px at 58% 55%, rgba(190,150,140,0.35) 0%, rgba(190,150,140,0) 100%),
      radial-gradient(ellipse 180px 200px at 22% 60%, rgba(170,150,160,0.30) 0%, rgba(170,150,160,0) 100%),
      linear-gradient(90deg, var(--photo-cream) 0%, var(--photo-peach) 45%, var(--photo-rose) 80%, #d3b5aa 100%);
  }
  .cover--orange .cover__photo {
    background:
      linear-gradient(180deg, rgba(236,122,56,0) 25%, rgba(236,122,56,0.55) 60%, var(--brand-orange) 92%),
      var(--scene);
  }
  .cover--navy .cover__photo {
    background:
      linear-gradient(180deg, rgba(39,53,77,0) 25%, rgba(110,110,140,0.45) 55%, rgba(39,53,77,0.85) 85%, var(--brand-navy) 100%),
      var(--scene);
  }
  .cover--blue .cover__photo {
    background:
      linear-gradient(180deg, rgba(20,90,168,0) 30%, rgba(150,165,215,0.5) 60%, rgba(20,90,168,0.9) 85%, var(--brand-blue) 100%),
      var(--scene);
  }

  .cover__brand {
    position: absolute;
    left: 147px;
    top: 126px;
    display: flex;
    align-items: center;
    gap: 20px;
  }
  .cover__mark {
    width: 121px;
    height: 121px;
    border-radius: 50%;
    background: var(--brand-orange);
    box-shadow: 0 2px 10px rgba(0,0,0,0.12);
    flex: none;
  }
  .cover__name {
    font-family: "Montserrat", sans-serif;
    font-weight: 700;
    font-size: 48px;
    letter-spacing: 2px;
    color: var(--text-light);
    text-transform: uppercase;
    white-space: nowrap;
    line-height: 1;
  }
  .cover__tagline {
    position: absolute;
    left: 164px;
    top: 274px;
    font-family: "Noto Sans", sans-serif;
    font-weight: 400;
    font-size: 14px;
    line-height: 21px;
    color: var(--text-light);
    white-space: nowrap;
  }
</style>
</head>
<body>
<main class="canvas">

  <section class="cover cover--orange">
    <div class="cover__photo" role="img" aria-label="Photo of a business meeting: two professionals shaking hands across a table while colleagues smile, bright window behind, fading into orange"></div>
    <div class="cover__brand">
      <div class="cover__mark"></div>
      <span class="cover__name">Corvane Group</span>
    </div>
    <p class="cover__tagline">Lorem ipsum dolor sit amet, consectetur adipiscing elit, sed do eiusmod tempor incididunt<br>ut labore et dolore magna aliqua. Quis ipsum suspendisse ultrices gravida. Risus commodo</p>
  </section>

  <section class="cover cover--navy">
    <div class="cover__photo" role="img" aria-label="Photo of a business meeting: two professionals shaking hands across a table while colleagues smile, bright window behind, fading into navy"></div>
    <div class="cover__brand">
      <div class="cover__mark"></div>
      <span class="cover__name">Corvane Group</span>
    </div>
    <p class="cover__tagline">Lorem ipsum dolor sit amet, consectetur adipiscing elit, sed do eiusmod tempor incididunt<br>ut labore et dolore magna aliqua. Quis ipsum suspendisse ultrices gravida. Risus commodo</p>
  </section>

  <section class="cover cover--blue">
    <div class="cover__photo" role="img" aria-label="Photo of a business meeting: two professionals shaking hands across a table while colleagues smile, bright window behind, fading into blue"></div>
    <div class="cover__brand">
      <div class="cover__mark"></div>
      <span class="cover__name">Corvane Group</span>
    </div>
    <p class="cover__tagline">Lorem ipsum dolor sit amet, consectetur adipiscing elit, sed do eiusmod tempor incididunt<br>ut labore et dolore magna aliqua. Quis ipsum suspendisse ultrices gravida. Risus commodo</p>
  </section>

</main>
</body>
</html>
```